For Creative Minds: A Simple Clean Book Cover that Stands Out

This will be a christian book teaching christians about divine healing. It is part of a series called "Forty Morning Set". I want the book cover to communicate the idea of healing, and specifically heavenly healing from God. These are some of the specifications below

1. General
Book to be published on print lantern platform
Dimensions: 6 x 9 inches, Paperback
Number of words: Estimated to be about 60,000 words.
Please use Indesign for design and submit the final Indesign source files along with the final design.

2. Cover image.
Image can be either human or any object that can communicate the idea above. No human faces to show up prominently.
High quality image is highly solicited.

3. Title:
" Forty Mornings to Claim and Hold Your Heavenly Restoration"

3. Author name
Preferably should appear below. Open to creative ideas with titles that are better placed above.

Author's Name: Daniel Fesch

3. Layout
Should not be too busy.
Simple and clean layout appeals more to me.

4. Series name
AS noted above, this book will be part of a series called " Forty Morning Set". I want this series name to appear somewhere in the cover and to have a simple but unique design that will be used for all subsequent titles. The Title of the book should have the emphasis.

I have attached a sample cover for one of my monthly devotional books which I choose from a contest.

ABOUT THE AUTHOR
Daniel Fesch represents the blessed combination of Physician and Minister, bringing healing not only to the physical body but to the spiritual heart. He currently works as the Director of the Hospital Medicine Program at the Brellmont County Care Campus in Iowa, USA. He is the Founder of Lantern & Vine Fellowship, a teaching ministry that seeks to bring believers into the fullness of grace — the glory of God — through conferences, seminars and books.

One of his notable quotes is “The Word of God is the most potent and efficient remedy for all the ailments of humanity.” This clearly portrays his experience with the Word as a Physician who is familiar with the powers, both natural and supernatural, to mend broken human beings. 

He currently lives in Iowa, USA with his wife, Tessa Lund, and daughter, Rosalind. You can reach out to Daniel using the contact information listed below.

BLURB
As a Physician and Minister, I have seen the power of modern medicine to bring about healing in the body and mind as well as the operation of the power of God to produce amazing medical results. However, many people are just not aware of the reality of divine healing. To some, it is a myth, belief or some "faith talk" in the heart. Medical miracles are real and we should take full advantage of it. As much as a love being a physician and treat patients in the hospital, I have come to see both its amazing successes and many limitations.

Industry/Entity Type

Christian

Font styles to use
Serif

Colors

Designer to choose colors to be used in the design.

Requirements
Should not have
• Too stylistic fonts

```html
<!DOCTYPE html>
<html lang="en">
<head>
<meta charset="utf-8">
<title>Forty Mornings to Claim and Hold Your Heavenly Restoration — Daniel Fesch</title>
<link rel="stylesheet" href="https://fonts.googleapis.com/css2?family=Cinzel:wght@400;500;600;700&display=swap">
<style>
  :root {
    --sky-top: #c7cbcf;
    --sky-haze: #f3eedb;
    --sun-gold: #f6d26a;
    --sun-amber: #e6a23c;
    --field-brown: #5a4726;
    --field-dark: #17110a;
    --night: #000000;
    --title-blue: #1d4c7a;
    --badge-fill: #f6d98c;
    --badge-ink: #7a4d22;
    --author-ink: #ffffff;
  }
  * { margin: 0; padding: 0; box-sizing: border-box; }
  html, body { width: 802px; height: 1200px; overflow: hidden; background: #000; }
  .cover {
    position: relative;
    width: 802px;
    height: 1200px;
    overflow: hidden;
    font-family: "Cinzel", "Times New Roman", serif;
  }
  .cover-photo {
    position: absolute;
    inset: 0;
    background:
      radial-gradient(ellipse 60% 28% at 62% 60%, rgba(255,240,170,0.85), rgba(255,240,170,0) 70%),
      linear-gradient(to bottom,
        var(--sky-top) 0%,
        var(--sky-haze) 28%,
        var(--sun-gold) 52%,
        var(--sun-amber) 66%,
        var(--field-brown) 76%,
        var(--field-dark) 88%,
        var(--night) 100%);
  }
  .series-badge {
    position: absolute;
    top: 27px;
    left: 300px;
    width: 216px;
    height: 37px;
    background: var(--badge-fill);
    color: var(--badge-ink);
    font-size: 15px;
    font-weight: 600;
    letter-spacing: 1.5px;
    display: flex;
    align-items: center;
    justify-content: center;
    text-transform: uppercase;
  }
  .book-title {
    position: absolute;
    top: 112px;
    left: 0;
    width: 100%;
    text-align: center;
    color: var(--title-blue);
    text-transform: uppercase;
    font-weight: 500;
    line-height: 1;
  }
  .book-title span { display: block; }
  .title-lead { font-size: 58px; font-weight: 600; margin-bottom: 18px; }
  .title-middle { font-size: 40px; margin-bottom: 14px; }
  .title-accent { font-size: 70px; margin-top: 8px; margin-bottom: 12px; }
  .author-name {
    position: absolute;
    top: 1108px;
    left: 0;
    width: 100%;
    text-align: center;
    color: var(--author-ink);
    font-size: 44px;
    font-weight: 500;
    letter-spacing: 2px;
    text-transform: uppercase;
  }
</style>
</head>
<body>
  <main class="cover">
    <div class="cover-photo" role="img" aria-label="Photograph of a person seen from behind standing in a tall grass field with arms outstretched toward a glowing golden sunrise sky"></div>
    <div class="series-badge">Forty Morning Set</div>
    <h1 class="book-title">
      <span class="title-lead">Forty Mornings</span>
      <span class="title-middle">To Claim and</span>
      <span class="title-middle">Hold Your</span>
      <span class="title-accent">Heavenly</span>
      <span class="title-accent">Restoration</span>
    </h1>
    <p class="author-name">Daniel Fesch</p>
  </main>
</body>
</html>
```